Dappled Perch Wild Bird Feeder Box Design

I’m looking for a professional box design for our Dappled Perch 38cm Wild Bird Feeder. The box should be predominantly white, with text and accent colours that match our supplied logo. I’ll provide the box cut-die and product images.
Front: Please feature the Dappled Perch logo, a large image of the feeder and the product name “38cm Wild Bird Feeder”. The feeder image must show the actual product accurately, including the feeding-port and perch positions. Images of UK wild birds can be used around the design.
Back: Please include information about the feeder and explain that customers can scan a QR code beside their chosen refill product to order it. We have 10 refill options to promote, with five shown on each of two panels. Each option needs its product image and corresponding QR code. Please also include an Vendora logo with the wording “All refills available on Vendora.”
Suggested description for the back:
“Bring wild birds closer to your garden with the Dappled Perch 38cm Wild Bird Feeder. Its clear tube lets you see when it’s time to refill, while the feeding ports and perches give visiting birds places to feed. Hang it in a suitable spot, fill it with your chosen wild bird food and enjoy watching the birds visit. Explore our range of refills by scanning the QR code beside your preferred product.”
Please include these details on the back:
Product code: DP500
EAN barcode: 5012345678900
Dimensions: 38cm high × 12.5cm wide
Company address: Corwell Traders, Fairbrook Road, Alton, GU12 7XT
Contact: Sales@corwelltraders.example
Please fit the finished design to the supplied cut-die and provide an editable Adobe Illustrator file, with the cut lines on a separate layer, plus print-ready exports. Please create the EAN barcode and QR codes as sharp, scannable artwork.

```html
<!DOCTYPE html>
<html lang="en">
<head>
<meta charset="utf-8">
<title>Dappled Perch 38cm Wild Bird Feeder – Box Panels</title>
<link href="https://fonts.googleapis.com/css2?family=Montserrat:wght@700;800&display=swap" rel="stylesheet">
<style>
  :root {
    --backdrop: #f4eee8;
    --panel-white: #ffffff;
    --panel-edge: #e4e0dc;
    --brand-teal: #178578;
    --brand-green: #7cb82a;
    --brand-green-light: #a3cd3d;
    --brand-green-deep: #5f9a1c;
    --seed-light: #d9a463;
    --seed-dark: #a8672d;
    --feeder-cap: #3a3a3a;
  }
  * { margin: 0; padding: 0; box-sizing: border-box; }
  html, body {
    width: 739px; height: 1200px; overflow: hidden;
    background: var(--backdrop);
    font-family: "Montserrat", Arial, sans-serif;
  }
  .box-layout { position: relative; width: 739px; height: 1200px; }

  .panel {
    position: absolute;
    background: var(--panel-white);
    border: 1px solid var(--panel-edge);
    overflow: hidden;
  }
  .panel--top   { left: 370px; top: 40px;  width: 300px; height: 300px; }
  .panel--side  { left: 70px;  top: 340px; width: 300px; height: 820px; }
  .panel--front { left: 370px; top: 340px; width: 300px; height: 820px; }

  .brand-mark {
    display: flex; align-items: center; gap: 10px;
    color: var(--brand-teal); font-weight: 800; white-space: nowrap;
  }
  .brand-mark__dot {
    width: 0.9em; height: 0.9em; border-radius: 50%;
    background: var(--brand-teal); flex: none;
  }

  .panel--top .brand-mark {
    position: absolute; left: 50%; top: 50%;
    transform: translate(-50%, -50%); font-size: 30px;
  }

  .panel--side .brand-mark {
    position: absolute; left: 150px; top: 390px;
    transform: translate(-50%, -50%) rotate(-90deg);
    font-size: 42px;
  }

  .panel--front .brand-mark {
    position: absolute; left: 80px; top: 55px; font-size: 22px;
  }

  .colour-wave { position: absolute; left: 0; bottom: 0; width: 100%; height: 300px; }

  .feeder-photo {
    position: absolute; left: 58px; top: 120px; width: 150px; height: 610px;
    border-radius: 14px;
    background: linear-gradient(180deg,
      var(--feeder-cap) 0, var(--feeder-cap) 6%,
      var(--seed-light) 6%, var(--seed-dark) 94%,
      var(--feeder-cap) 94%, var(--feeder-cap) 100%);
  }

  .product-name {
    position: absolute; right: 18px; bottom: 120px;
    writing-mode: vertical-rl; transform: rotate(180deg);
    font-size: 44px; font-weight: 800; line-height: 1; white-space: nowrap;
    color: var(--brand-green);
  }
  .product-name__size { color: var(--brand-teal); }
</style>
</head>
<body>
<main class="box-layout">

  <section class="panel panel--top" aria-label="Top panel">
    <div class="brand-mark"><span class="brand-mark__dot"></span>Dappled Perch</div>
  </section>

  <section class="panel panel--side" aria-label="Side panel">
    <div class="brand-mark"><span class="brand-mark__dot"></span>Dappled Perch</div>
    <svg class="colour-wave" viewBox="0 0 300 300" preserveAspectRatio="none" aria-hidden="true">
      <path d="M0 110 C60 70 90 60 120 90 C150 120 220 110 300 80 L300 300 L0 300 Z" fill="var(--brand-green-light)"/>
      <circle cx="60" cy="70" r="28" fill="var(--brand-green-light)"/>
      <path d="M0 160 C80 120 160 150 300 120 L300 300 L0 300 Z" fill="var(--brand-green)"/>
      <path d="M0 260 C90 200 180 230 300 150 L300 300 L0 300 Z" fill="var(--panel-white)"/>
    </svg>
  </section>

  <section class="panel panel--front" aria-label="Front panel">
    <svg class="colour-wave" viewBox="0 0 300 300" preserveAspectRatio="none" aria-hidden="true">
      <path d="M0 150 C80 130 180 60 300 20 L300 300 L0 300 Z" fill="var(--brand-green-light)"/>
      <path d="M0 190 C100 170 200 90 300 60 L300 300 L0 300 Z" fill="var(--brand-green)"/>
      <path d="M0 280 C120 240 220 170 300 130 L300 300 L0 300 Z" fill="var(--panel-white)"/>
    </svg>
    <div class="brand-mark"><span class="brand-mark__dot"></span>Dappled Perch</div>
    <div class="feeder-photo" role="img" aria-label="Photo of the 38cm tube bird feeder filled with seed, with feeding ports, perches and two wild birds perched on it"></div>
    <div class="product-name"><span class="product-name__size">38cm</span> Wild Bird Feeder</div>
  </section>

</main>
</body>
</html>
```